Disposable Mini Sauce Pot Design for Asian Chain Food Brands

We operate a Hainan Chicken Rice takeout brand under the name Wokly8, with our official website: www.Wokly8.com.
We offer four signature house sauces and are launching brand-new packaging for our sauce line. We require custom graphic designs exclusively for the sauce cup lids.
Product Material & Base Specs
The sauce cups are made of PP plastic, available in two translucent base options: Translucent White and Translucent Orange.
Four Sauce Varieties for Individual Lid Designs
1. Red Sauce – Fried Sweet Chili Sauce
2.Green Sauce – Scallion Oil Dressing
3.Sweet Soy Sauce
4.Sweet Red Sauce (Special for Fried Chicken)
Differentiate each sauce lid design through unique graphics, typography, or illustrative elements for easy customer identification.
The marking NET WT 2 OZ must be clearly printed on every lid.
**There is no need to print full descriptive text or the full name of the sauces on each lid; the design only needs to clearly differentiate the four sauce varieties.
**Please reference the original design style and brand color palette shown on our official website, and feel free to fully unleash your creativity.
Look and feel
Each slider illustrates characteristics of the customer's brand and the style your logo design should communicate.

```html
<!DOCTYPE html>
<html lang="en">
<head>
<meta charset="utf-8">
<title>Wokly8 Sauce Lid Series</title>
<link href="https://fonts.googleapis.com/css2?family=Bebas+Neue&family=Barlow+Condensed:wght@600;700&display=swap" rel="stylesheet">
<style>
  :root{
    --paper:#fbfbfb;
    --stage:#ece6df;
    --white:#ffffff;
    --red:#dc1c12; --red-deep:#8e0d08; --red-art-a:#f5501a; --red-art-b:#f7e4dc; --red-ink:#3b0704;
    --green:#8ab514; --green-deep:#22692b; --green-art-a:#2f7a2d; --green-art-b:#d9e8c4; --green-ink:#1b2c06;
    --orange:#f26a06; --orange-deep:#7a3208; --orange-art-a:#3a1408; --orange-art-b:#8a3a10; --orange-band:#e35d04; --orange-ink:#2d1204;
    --plum:#c4154f; --plum-deep:#7c0b32; --plum-art-a:#e8466f; --plum-art-b:#d81b4a; --plum-ink:#3a0516;
    --rim-white:#f4f2ef; --rim-orange:#f6a23a;
    --label:#6b6661;
  }
  *{margin:0;padding:0;box-sizing:border-box}
  html,body{width:854px;height:1200px;overflow:hidden}
  body{background:var(--stage);position:relative;font-family:"Barlow Condensed",sans-serif}

  .board{position:absolute;left:0;top:0;width:854px;height:598px;background:var(--paper)}

  .lid{position:absolute;width:331px;height:270px;border-radius:38px;overflow:hidden;color:var(--white)}
  .lid::after{content:"";position:absolute;right:0;top:0;width:52px;height:52px;background:var(--fold);clip-path:polygon(0 0,100% 100%,100% 0);z-index:3}
  .lid--red{background:var(--red);--fold:var(--red-deep);--ink:var(--red-ink)}
  .lid--green{background:var(--green);--fold:var(--green-deep);--ink:var(--green-ink)}
  .lid--orange{background:var(--orange);--fold:var(--orange-deep);--ink:var(--orange-ink)}
  .lid--plum{background:var(--plum);--fold:var(--plum-deep);--ink:var(--plum-ink)}

  .brand{position:absolute;left:27px;top:16px;font-family:"Bebas Neue",sans-serif;font-size:46px;line-height:1;color:var(--white);letter-spacing:1px;z-index:2}
  .brand-tag{position:absolute;left:28px;top:60px;font-size:10px;font-weight:700;letter-spacing:.3px;color:var(--ink);z-index:2}
  .title{position:absolute;left:26px;top:76px;font-family:"Bebas Neue",sans-serif;font-size:66px;line-height:.86;color:var(--white);z-index:2;white-space:nowrap}
  .title .second{font-size:58px}
  .subtitle{position:absolute;left:28px;top:199px;font-size:14px;font-weight:700;line-height:1.05;color:var(--ink);z-index:2}
  .netwt{position:absolute;left:0;right:0;bottom:9px;text-align:center;font-size:13px;font-weight:700;color:var(--white);z-index:2;letter-spacing:.3px}

  .art{position:absolute;z-index:1}
  .art--chili{left:178px;top:20px;width:153px;height:230px;background:linear-gradient(160deg,var(--red-art-a),var(--red-art-b))}
  .art--scallion{left:186px;top:20px;width:145px;height:230px;background:linear-gradient(200deg,var(--green-art-a),var(--green-art-b))}
  .art--bowl{left:204px;top:50px;width:127px;height:180px;background:linear-gradient(180deg,var(--orange-art-b),var(--orange-art-a))}
  .band--wood{position:absolute;left:0;right:0;bottom:0;height:62px;background:var(--orange-band)}
  .art--rooster{left:190px;top:20px;width:141px;height:250px;background:linear-gradient(180deg,var(--plum-art-a),var(--plum-art-b))}

  .pos-1{left:71px;top:44px}.pos-2{left:454px;top:44px}.pos-3{left:71px;top:332px}.pos-4{left:454px;top:332px}

  .mini{position:absolute;width:184px;height:170px}
  .mini .lid{left:0;top:0;transform:scale(.556);transform-origin:top left}
  .mini .rim{position:absolute;left:4px;top:148px;width:176px;height:12px;border-radius:0 0 10px 10px}
  .row-white .rim{background:var(--rim-white)}
  .row-orange .rim{background:var(--rim-orange)}

  .row-label{position:absolute;left:0;width:854px;text-align:center;font-size:18px;font-weight:700;letter-spacing:1.5px;color:var(--label)}
</style>
</head>
<body>
<section class="board">
  <div class="lid lid--red pos-1">
    <div class="art art--chili" role="img" aria-label="Illustration: white chili pepper in orange flames"></div>
    <div class="brand">Wokly8</div><div class="brand-tag">HAINAN CHICKEN</div>
    <div class="title">RED<br>SAUCE</div>
    <div class="subtitle">FRIED SWEET<br>CHILI SAUCE</div>
    <div class="netwt">NET WT 2 OZ</div>
  </div>
  <div class="lid lid--green pos-2">
    <div class="art art--scallion" role="img" aria-label="Illustration: scallion stalk with oil drops"></div>
    <div class="brand">Wokly8</div><div class="brand-tag">HAINAN CHICKEN</div>
    <div class="title">GREEN<br>SAUCE</div>
    <div class="subtitle">SCALLION OIL<br>DRESSING</div>
    <div class="netwt">NET WT 2 OZ</div>
  </div>
  <div class="lid lid--orange pos-3">
    <div class="band--wood" role="img" aria-label="Wood grain table pattern"></div>
    <div class="art art--bowl" role="img" aria-label="Illustration: bowl of soy sauce with a splashing drop"></div>
    <div class="brand">Wokly8</div><div class="brand-tag">HAINAN CHICKEN</div>
    <div class="title">SWEET<br><span class="second">SOY SAUCE</span></div>
    <div class="netwt">NET WT 2 OZ</div>
  </div>
  <div class="lid lid--plum pos-4">
    <div class="art art--rooster" role="img" aria-label="Illustration: rooster silhouette with a red chili pepper"></div>
    <div class="brand">Wokly8</div><div class="brand-tag">HAINAN CHICKEN</div>
    <div class="title">SWEET<br>RED SAUCE</div>
    <div class="subtitle">SPECIAL FOR<br>FRIED CHICKEN</div>
    <div class="netwt">NET WT 2 OZ</div>
  </div>
</section>

<section class="row-white">
  <div class="mini" style="left:33px;top:689px"><div class="rim"></div><div class="lid lid--red"><div class="art art--chili" role="img" aria-label="Illustration: chili pepper in flames"></div><div class="brand">Wokly8</div><div class="brand-tag">HAINAN CHICKEN</div><div class="title">RED<br>SAUCE</div><div class="subtitle">FRIED SWEET<br>CHILI SAUCE</div><div class="netwt">NET WT 2 OZ</div></div></div>
  <div class="mini" style="left:233px;top:689px"><div class="rim"></div><div class="lid lid--green"><div class="art art--scallion" role="img" aria-label="Illustration: scallion stalk"></div><div class="brand">Wokly8</div><div class="brand-tag">HAINAN CHICKEN</div><div class="title">GREEN<br>SAUCE</div><div class="subtitle">SCALLION OIL<br>DRESSING</div><div class="netwt">NET WT 2 OZ</div></div></div>
  <div class="mini" style="left:433px;top:689px"><div class="rim"></div><div class="lid lid--orange"><div class="band--wood" role="img" aria-label="Wood grain pattern"></div><div class="art art--bowl" role="img" aria-label="Illustration: soy sauce bowl"></div><div class="brand">Wokly8</div><div class="brand-tag">HAINAN CHICKEN</div><div class="title">SWEET<br><span class="second">SOY SAUCE</span></div><div class="netwt">NET WT 2 OZ</div></div></div>
  <div class="mini" style="left:630px;top:689px"><div class="rim"></div><div class="lid lid--plum"><div class="art art--rooster" role="img" aria-label="Illustration: rooster silhouette with chili"></div><div class="brand">Wokly8</div><div class="brand-tag">HAINAN CHICKEN</div><div class="title">SWEET<br>RED SAUCE</div><div class="subtitle">SPECIAL FOR<br>FRIED CHICKEN</div><div class="netwt">NET WT 2 OZ</div></div></div>
  <div class="row-label" style="top:892px">TRANSLUCENT WHITE</div>
</section>

<section class="row-orange">
  <div class="mini" style="left:33px;top:944px"><div class="rim"></div><div class="lid lid--red"><div class="art art--chili" role="img" aria-label="Illustration: chili pepper in flames"></div><div class="brand">Wokly8</div><div class="brand-tag">HAINAN CHICKEN</div><div class="title">RED<br>SAUCE</div><div class="subtitle">FRIED SWEET<br>CHILI SAUCE</div><div class="netwt">NET WT 2 OZ</div></div></div>
  <div class="mini" style="left:233px;top:944px"><div class="rim"></div><div class="lid lid--green"><div class="art art--scallion" role="img" aria-label="Illustration: scallion stalk"></div><div class="brand">Wokly8</div><div class="brand-tag">HAINAN CHICKEN</div><div class="title">GREEN<br>SAUCE</div><div class="subtitle">SCALLION OIL<br>DRESSING</div><div class="netwt">NET WT 2 OZ</div></div></div>
  <div class="mini" style="left:433px;top:944px"><div class="rim"></div><div class="lid lid--orange"><div class="band--wood" role="img" aria-label="Wood grain pattern"></div><div class="art art--bowl" role="img" aria-label="Illustration: soy sauce bowl"></div><div class="brand">Wokly8</div><div class="brand-tag">HAINAN CHICKEN</div><div class="title">SWEET<br><span class="second">SOY SAUCE</span></div><div class="netwt">NET WT 2 OZ</div></div></div>
  <div class="mini" style="left:630px;top:944px"><div class="rim"></div><div class="lid lid--plum"><div class="art art--rooster" role="img" aria-label="Illustration: rooster silhouette with chili"></div><div class="brand">Wokly8</div><div class="brand-tag">HAINAN CHICKEN</div><div class="title">SWEET<br>RED SAUCE</div><div class="subtitle">SPECIAL FOR<br>FRIED CHICKEN</div><div class="netwt">NET WT 2 OZ</div></div></div>
  <div class="row-label" style="top:1148px">TRANSLUCENT ORANGE</div>
</section>
</body>
</html>
```